Business Card Design

Divorce
Collaborative Family Law
Family Dispute Resolution
Family Law Property & Children

Target Market(s)

Australia

Industry/Entity Type

Business

Contact Information for Business Card

Delia Frampton
M App Law (Family Law) LLB (Hons) BA (Hons) Ass Dip Ag (HH)
Family Dispute Resolution Provider
Frampton Family Law
PO Box 4372 Wendlebury 3914
Phone 03 57218300 Fax 03 57218399 Email framptonfamilylaw@quillmail.example

Colors
f04a51

Requirements
Should not have
• Any reference to
United States or US terminology
the word Company

```html
<!DOCTYPE html>
<html lang="en">
<head>
<meta charset="utf-8">
<title>Frampton Family Law – Business Card</title>
<link rel="stylesheet" href="https://fonts.googleapis.com/css2?family=Lato:wght@400;700;900&display=swap">
<style>
  :root {
    --backdrop: #e9e6e1;
    --card-navy: #27266d;
    --card-ink: #ffffff;
    --card-ink-soft: #eceaf6;
  }
  * { box-sizing: border-box; margin: 0; padding: 0; }
  html, body {
    width: 1200px;
    height: 870px;
    overflow: hidden;
    background: var(--backdrop);
  }
  .canvas {
    width: 1200px;
    height: 870px;
    display: flex;
    align-items: center;
    justify-content: center;
  }
  .business-card {
    width: 470px;
    height: 770px;
    background: var(--card-navy);
    color: var(--card-ink);
    font-family: "Lato", sans-serif;
    display: flex;
    flex-direction: column;
    align-items: center;
    text-align: center;
    padding-top: 170px;
  }
  .brand-mark {
    display: flex;
    align-items: center;
    gap: 12px;
    font-size: 24px;
    font-weight: 400;
    letter-spacing: 0.06em;
    color: var(--card-ink);
  }
  .brand-mark__dot {
    width: 14px;
    height: 14px;
    border-radius: 50%;
    background: var(--card-ink);
  }
  .holder {
    margin-top: 130px;
  }
  .holder__name {
    font-size: 27px;
    font-weight: 900;
    letter-spacing: 0.07em;
    text-transform: uppercase;
  }
  .holder__direct {
    margin-top: 4px;
    font-size: 19px;
    letter-spacing: 0.08em;
    color: var(--card-ink-soft);
  }
  .contact {
    margin-top: 86px;
    font-size: 19px;
    line-height: 1.55;
    letter-spacing: 0.06em;
    color: var(--card-ink-soft);
    list-style: none;
  }
  .contact__email {
    font-size: 17px;
    letter-spacing: 0.03em;
  }
</style>
</head>
<body>
  <main class="canvas">
    <article class="business-card">
      <div class="brand-mark">
        <span class="brand-mark__dot" aria-hidden="true"></span>
        <span class="brand-mark__name">Frampton Family Law</span>
      </div>

      <header class="holder">
        <h1 class="holder__name">Delia Frampton</h1>
        <p class="holder__direct">03 57218399</p>
      </header>

      <ul class="contact">
        <li class="contact__firm">Frampton Family Law</li>
        <li class="contact__address">PO Box 4372 Wendlebury 3914</li>
        <li class="contact__email">framptonfamilylaw@quillmail.example</li>
        <li class="contact__phone">03 57218300</li>
      </ul>
    </article>
  </main>
</body>
</html>
```